Commercial Cleaning Company specializing in windows and floors

Looking to have a brochure made for commercial cleaning company. Services include 2 categories:
1. Window Washing

2. Floor Cleaning and Restoration.

Within floor and cleaning restoration, there are several categories:
Carpet Cleaning & Restoration
-Tile and Grout Cleaning & Restoration
-Concrete Cleaning & Restoration
-Stone Cleaning & Restoration (Terrazzo, Marble, Limestone)
-VCT Cleaning & Restoration
-Wood Floor Cleaning & Restoration
-Epoxy Floor Cleaning & Restoration
Floor cleaning Text:
FLOOR CARE:

CARPET FLOORS
Low Moisture, Safe & Fast <--- Increase Font and color
Designed to support a healthy indoor environment, our carpet cleaning methods will eliminate the most common problems caused by other cleaning methods that lead to mold growth, mildew, volatile organic compounds (VOC), insufficient drying times, recurring stains and safety hazards. We also mitigate common safety hazards associated with multiple lengthy hoses, insecure open doors, and slippery hard surfaces. You'll find our system also eliminates both noise and emission pollution around your facility during cleaning times that are common with other cleaning methods.
Our low-moisture system supports a healthy indoor environment so carpets will stay clean & vibrant in color. With superior drying times, our methods eliminates mold growth and mildew. When we are finished cleaning, all that’s left are incredibly clean and fresh smelling carpets

TILE & GROUT FLOORS
We get deep into our cleaning <--- Increase Font and color
Tile and Grout floors can be very difficult to maintain. Often, dirt and grime get trapped in grout lines and crevices and discolor them, making the floors appear dirty. Our company has done all the experimenting for you, and we know the correct brushes, weight kits, machines, and chemical combinations to use to restore and maintain these types of floors, without leaving residue behind that will cause soil to return.

CONCRETE FLOORS
Pores & Crevices are no match <--- Increase Font and color
When it comes to scrubbing and cleaning concrete surfaces such as school hallways, patios, and other types of high traffic concrete flooring, we have you covered.
We're here to keep your employees and visitors safer. We eliminate having to use harsh chemicals and abundances of water to remove the heavy soil that has settled deep down in the concrete pores and crevices.

STONE FLOORS - TERRAZZO, MARBLE, LIMESTONE
We are experts in protecting your major flooring investment. <--- Increase Font and color
If you have high end stone floors, make sure they are performing their best for your facility. We can make educated recommendations on restoration schedules, cleaning methods, schedules, matting and everything related to making your floors "pop". These multi-step processes can be complex, but our experience ensures the best result for your building.

WOOD FLOORS
Wood floors can be tricky - We know how to clean and refinish them. <--- Increase Font and color
If you aren't careful, you may end up with undesirable results when dealing with wood floors. Traditional swing machines can leave swirls if not used correctly, and other methods may damage the wood. We've trained with leading wood floor companies to ensure a process that's safe for your floors and bring you the results you're looking for.

EPOXY FLOORS
We Clean Terrazzo, Flake coating, Screeds & More <--- Increase Font and color

Epoxy is protected from chemicals, dirt, liquids and other contaminants, however, Epoxy floors need to be cleaned routinely as they lose their original luster. We can restore any type of Epoxy floor and bring them back to life.

VCT/VINYL FLOORS <--- Increase Font and color

The most common floor types are our specialty
We can assist you in the maintenance of VCT and vinyl floors. We are helpful resources for assistance with stripping and re coating, daily maintenance, burnishing, and restorative buffing. We have worked with major pad manufacturers and chemical companies to help make selections on the best possible floor maintenance system for these common floors.

Window cleaning Text:
WINDOW CARE:
Our goal is to leave your employees and visitors with the best possible impression of your facility, and clean windows are a huge part of that. BrightHollow uses the latest pure water technology and equipment to leave your windows sparkling clean. We are trained to identify the correct process for various interior and exterior windows, as well as performing restorative processes for things like hard water deposits.
Older cleaning methods often leave behind streaking or residues. Brighthollow has invested in equipment that utilizes de-ionized water, microfibers, and state of the art filtration. Recent designs in pole construction allow us to access hard to reach windows, facades, solar panels, sills, and ledges without the use of heavy equipment.
We offer a spate of maintenance programs the ensure the lowest total cost of cleaning. Inquire with us to learn more about why contracting these important cleaning tasks to Brighthollows will relieve you of: equipment storage and maintenance , brush selection, filtration concerns - as well as the liability of work that can sometimes present danger to untrained employees.

Company Biography Page:

BrightHollow is a family based company located in the greater Houston area that specializes in commercial floor care and window cleaning. Our mission is to prioritize the health and safety of the people who use your building by offering cleaning methods that are safe and use the latest industry technology. We understand that a clean, well maintained building has a direct relationship with your image - and that can have a direct effect on your bottom line or reputation. Please consider us for further consultation if you are interested in a no obligation discussion about your facility.

The management of BrightHollow has spent their entire professional lives in the commercial cleaning industry. We have recently sold facility supply distribution company and understand the facility maintenance industry top to bottom. In that time, we've met with innumerable manufacturers, distributors, trade groups, trainers and end users to gain insight into national and regional cleaning trends and methods. We understand budgets, compliance requirements, workflow timelines, and restorative schedules that you don't typically find in a contract cleaning company.
We are confident you will benefit from our wide range of experience and expertise when it comes to maintaining your facility.

Layout:

I think it would work best to have a 4 page single fold booklet type brochure - but open to any suggestions.
The inside would have the 2 services - one side hard floors and the other side windows. Either the front or the back would have our biography on it (probably the back?).
I will give you more input like the address and phone number at the end, it can be added easily.

For the pictures I've added:
The ones that include the word "example" are to be used when incorporating the services.

I've also included a bunch of window pictures. You can use some or none of these (and get other ones) in companion with the text about window cleaning.

Target Market(s)

Commercial buildings and institutions looking for our specific cleaning services

Industry/Entity Type

Commercial Cleaning

Font styles to use
Serif
Sans Serif

Colors
0054AA
0677BA
7BADD7
CADEEF
E8F1F8
0094D4
00A9DD
6FCCEA
C7EBF8
E9F6FB
59FF00
82FF00
B8FF75
E3FFCB
F4FFEA

Requirements
Must have
• All of the included text (can be edited slightly)
Nice to have
• Additional images or text gleened from other sources or past experience that help communicate our business

```html
<!DOCTYPE html>
<html lang="en">
<head>
<meta charset="utf-8">
<title>BrightHollow Brochure</title>
<link href="https://fonts.googleapis.com/css2?family=League+Gothic&family=Lato:ital,wght@0,400;0,700;1,400;1,700&display=swap" rel="stylesheet">
<style>
:root{
  --stage:#dcdcdc;
  --paper:#ffffff;
  --blue:#3d6cc2;
  --blue-text:#3566b8;
  --navy:#1f3a78;
  --green-dark:#1c321d;
  --ink:#1d1d1d;
  --row:#e4e4e4;
  --black:#0a0a0a;
}
*{margin:0;padding:0;box-sizing:border-box}
html,body{width:838px;height:1200px;overflow:hidden}
body{background:var(--stage);position:relative;font-family:"Lato",sans-serif;color:var(--ink)}
.page{position:absolute;background:var(--paper);overflow:hidden;box-shadow:0 2px 6px rgba(0,0,0,.25)}
.page-cover{left:39px;top:65px;width:371px;height:519px}
.page-windows{left:431px;top:65px;width:369px;height:519px}
.page-floors{left:39px;top:616px;width:371px;height:522px}
.page-bio{left:431px;top:616px;width:369px;height:519px}
.abs{position:absolute}
.photo{position:absolute}
.brand{position:absolute;display:flex;align-items:center;gap:5px;font-family:"Lato",sans-serif;font-weight:700;color:var(--navy);white-space:nowrap}
.brand .dot{border-radius:50%;background:var(--navy);flex:none}
.display{font-family:"League Gothic",sans-serif;font-weight:400;text-transform:uppercase;line-height:1;white-space:nowrap}

/* cover */
.cover-hero{left:0;top:0;width:371px;height:316px;background:linear-gradient(160deg,#f4f7fb 0%,#bcd0ea 28%,#4a74b2 55%,#102a55 85%,#0a1a36 100%)}
.cover-brand{left:0;right:0;top:28px;justify-content:center;font-size:22px}
.cover-brand .dot{width:12px;height:12px}
.cover-band{left:0;top:316px;width:371px;height:84px;background:var(--blue)}
.cover-thumb{top:328px;height:63px;width:115px}
.cover-foot{left:0;top:400px;width:371px;height:119px;background:linear-gradient(#f2f4f7,#ffffff)}
.cover-title{left:0;right:0;top:438px;text-align:center;font-size:27px;color:var(--blue-text)}
.cover-url{left:85px;top:474px;width:196px;height:30px;background:var(--black);color:#fff;display:flex;align-items:center;justify-content:center;font-size:19px}

/* windows */
.win-hero{left:0;top:0;width:369px;height:135px;background:linear-gradient(120deg,#0f3a78,#3f86c9 40%,#a8cdee 60%,#2d5f9e 85%,#153c6e)}
.win-rail{left:232px;top:135px;width:137px;height:384px;background:var(--green-dark)}
.win-thumb{left:239px;width:122px;border:1px solid #c9d2c9}
.win-title{left:0;top:159px;width:163px;height:27px;background:var(--green-dark);color:#fff;font-size:24px;padding-left:14px;display:flex;align-items:center}
.win-copy{left:16px;top:200px;width:200px;font-size:6.9px;line-height:9.4px;text-align:justify}
.win-copy p+p{margin-top:9.4px}
.win-brand{left:16px;top:466px;font-size:17px}
.win-brand .dot{width:9px;height:9px}

/* floors */
.carpet-box{left:0;top:0;width:219px;height:134px;background:var(--blue);color:#fff;padding:10px 10px 0 10px}
.carpet-head{font-size:8.3px;font-weight:700;display:flex;align-items:center;gap:3px;white-space:nowrap}
.carpet-head em{font-weight:700;font-size:6.8px}
.carpet-copy{margin-top:3px;font-size:5.3px;line-height:7.7px;text-align:justify;font-weight:400}
.floor-panel{left:219px;top:0;width:152px;height:124px;background:var(--green-dark)}
.floor-title{left:227px;top:9px;color:#fff;font-size:27px}
.floor-photo{left:225px;top:40px;width:140px;height:79px;background:linear-gradient(#d6d9dc 0%,#c3c7cb 45%,#3a3d42 60%,#22252a 100%)}
.floor-row{position:absolute;left:11px;width:350px;background:var(--row)}
.floor-row .pic{position:absolute;left:4px;top:5px;width:83px;border:1px solid #3d6cc2}
.floor-row .txt{position:absolute;left:99px;top:6px;right:10px}
.floor-row h3{font-size:8.3px;font-weight:700;line-height:10.5px;display:flex;flex-wrap:wrap;align-items:baseline}
.floor-row h3 .arrow{font-size:6px;margin-right:3px}
.floor-row h3 em{font-weight:400;color:var(--blue-text);font-size:8.3px}
.floor-row h3 .sep{color:var(--blue-text);font-weight:400;margin:0 3px}
.floor-row h3 .line2{flex-basis:100%;font-style:italic;font-weight:400;color:var(--blue-text)}
.floor-row p{margin-top:2px;font-size:5.4px;line-height:7px}

/* bio */
.bio-head{left:0;top:0;width:369px;height:66px;background:var(--blue);color:#fff;display:flex;align-items:center;justify-content:center;font-size:28px}
.bio-copy{left:16px;top:85px;width:337px;font-size:6.9px;line-height:9.4px;text-align:justify}
.bio-copy p+p{margin-top:9.4px}
.bio-brand{left:197px;top:250px;font-size:20px}
.bio-brand .dot{width:11px;height:11px}
.bio-photo{left:0;top:332px;width:369px;height:187px;background:linear-gradient(180deg,#ffffff 0%,#dbe3ec 30%,#9fb4cc 60%,#4f6c91 100%)}
.contact-box{left:12px;top:332px;width:138px;height:187px;background:var(--black)}
.contact-label{left:19px;top:342px;width:123px;height:23px;background:var(--blue);color:#fff;display:flex;align-items:center;justify-content:center;font-size:19px;letter-spacing:3px}
</style>
</head>
<body>

<section class="page page-cover">
  <div class="photo cover-hero" role="img" aria-label="Glass office tower facade reflecting blue sky"></div>
  <div class="brand cover-brand"><span class="dot"></span>BrightHollow</div>
  <div class="abs cover-band"></div>
  <div class="photo cover-thumb" style="left:9px;background:linear-gradient(#e6e8ea 0%,#bfc3c6 45%,#6c7075 100%)" role="img" aria-label="Office with patterned grey carpet tiles"></div>
  <div class="photo cover-thumb" style="left:128px;background:linear-gradient(#eef0f2 0%,#b9bec4 50%,#b54a4a 70%,#9aa1a8 100%)" role="img" aria-label="Airport lounge with red seating on polished floor"></div>
  <div class="photo cover-thumb" style="left:247px;background:linear-gradient(90deg,#c9a77a 0%,#7fa4c9 35%,#b8d0e6 70%,#6e8fb3 100%)" role="img" aria-label="Curved glass window wall of a building"></div>
  <div class="abs cover-foot"></div>
  <h1 class="abs display cover-title">Commercial Floor Care &amp; Window Cleaning</h1>
  <div class="abs display cover-url">www.brighthollow.com</div>
</section>

<section class="page page-windows">
  <div class="photo win-hero" role="img" aria-label="Collage of window cleaners with squeegees and water-fed poles"></div>
  <div class="abs win-rail"></div>
  <div class="photo win-thumb" style="top:142px;height:87px;background:linear-gradient(90deg,#d9dde0,#9fb0bf 40%,#e9eef2 70%,#8fa37a)" role="img" aria-label="Interior glass wall overlooking a lawn"></div>
  <div class="photo win-thumb" style="top:235px;height:87px;background:linear-gradient(150deg,#cfe2ec,#7fa6bf 45%,#4c7a56 70%,#a9c7d8)" role="img" aria-label="Squeegee wiping a soapy window"></div>
  <div class="photo win-thumb" style="top:328px;height:87px;background:linear-gradient(160deg,#9fb5c8,#5b6f82 40%,#a06a48 65%,#3e4d5c)" role="img" aria-label="Building facade with rows of reflective windows"></div>
  <div class="photo win-thumb" style="top:421px;height:90px;background:linear-gradient(200deg,#c8dbe9,#5d86ad 40%,#2c4a6a 75%,#8fb1cd)" role="img" aria-label="Window cleaner working on a tilted glass facade"></div>
  <h2 class="abs display win-title">Window Cleaning</h2>
  <div class="abs win-copy">
    <p>Our goal is to leave your employees and visitors with the best possible impression of your facility, and clean windows are a huge part of that.</p>
    <p>BrightHollow uses the latest pure water technology and equipment to leave your windows sparkling clean. We are trained to identify the correct process for various interior and exterior windows, as well as performing restorative processes for things like hard water deposits.</p>
    <p>Older cleaning methods often leave behind streaking or residues. Brighthollow has invested in equipment that utilizes de-ionized water, microfibers, and state of the art filtration. Recent designs in pole construction allow us to access hard to reach windows, facades, solar panels, sills, and ledges without the use of heavy equipment.</p>
    <p>We offer a spate of maintenance programs the ensure the lowest total cost of cleaning. Inquire with us to learn more about why contracting these important cleaning tasks to Brighthollows will relieve you of: equipment storage and maintenance, brush selection, filtration concerns - as well as the liability of work that can sometimes present danger to untrained employees</p>
  </div>
  <div class="brand win-brand"><span class="dot"></span>BrightHollow</div>
</section>

<section class="page page-floors">
  <div class="abs carpet-box">
    <h3 class="carpet-head"><span style="font-size:6px">&#9654;</span>CARPET FLOORS | <em>Low Moisture, Safe &amp; Fast</em></h3>
    <p class="carpet-copy">Designed to support a healthy indoor environment, our carpet cleaning methods will eliminate the most common problems caused by other cleaning methods that lead to mold growth, mildew, volatile organic compounds (VOC), insufficient drying times, recurring stains &amp; safety hazards. We also mitigate common safety hazards associated with multiple lengthy hoses, insecure open doors, and slippery hard surfaces. You'll find our system also eliminates both noise &amp; emission pollution around your facility during cleaning times that are common with other cleaning methods. Our low-moisture system supports a healthy indoor environment so carpets will stay clean &amp; vibrant in color. With superior drying times, our methods eliminates mold growth &amp; mildew. When we are finished cleaning, all that's left are incredibly clean &amp; fresh smelling carpets</p>
  </div>
  <div class="abs floor-panel"></div>
  <h2 class="abs display floor-title">Floor Care</h2>
  <div class="photo floor-photo" role="img" aria-label="Chairs on patterned grey carpet tiles"></div>

  <div class="floor-row" style="top:143px;height:58px">
    <div class="photo pic" style="height:48px;background:linear-gradient(90deg,#f1f1f1,#c23a3a 35%,#e9e9e9 60%,#c9cdd1)" role="img" aria-label="Restroom with red stall doors and tiled floor"></div>
    <div class="txt">
      <h3><span class="arrow">&#9654;</span>TILE &amp; GROUT FLOORS<span class="sep">|</span><em>We get deep into our cleaning</em></h3>
      <p>Tile and Grout floors can be very difficult to maintain. Our company has done all the experimenting for you, and we know the correct brushes, weight kits, machines, and chemical combinations to use to restore and maintain these types of floors, without leaving residue behind that will cause soil to return.</p>
    </div>
  </div>

  <div class="floor-row" style="top:205px;height:59px">
    <div class="photo pic" style="height:49px;background:linear-gradient(90deg,#b8c6d4,#e8eef2 40%,#c0393d 65%,#9aa6b2)" role="img" aria-label="Lobby with red sofas on polished concrete"></div>
    <div class="txt">
      <h3><span class="arrow">&#9654;</span>CONCRETE FLOORS<span class="sep">|</span><em>Pores &amp; Crevices are no match</em></h3>
      <p>When it comes to scrubbing and cleaning concrete surfaces such as school hallways, patios, and other types of high traffic concrete flooring, we have you covered. We're here to keep your employees and visitors safer. We eliminate having to use harsh chemicals &amp; abundances of water to remove the heavy soil that has settled deep down in the concrete pores &amp; crevices.</p>
    </div>
  </div>

  <div class="floor-row" style="top:267px;height:60px">
    <div class="photo pic" style="height:50px;background:linear-gradient(#e4e7ea,#a9b0b7 45%,#b54545 62%,#d5d9dd)" role="img" aria-label="Terminal hall with rows of seating on stone floor"></div>
    <div class="txt">
      <h3><span class="arrow">&#9654;</span>STONE FLOORS - TERRAZZO, MARBLE, LIMESTONE<span class="line2">| We are experts in protecting your major flooring investment.</span></h3>
      <p>We can make educated recommendations on restoration schedules, cleaning methods, schedules, matting and everything related to making your floors "pop". These multi-step processes can be complex, but our experience ensures the best result for your building</p>
    </div>
  </div>

  <div class="floor-row" style="top:331px;height:57px">
    <div class="photo pic" style="height:47px;background:linear-gradient(#f2f0ec,#e2ddd5 50%,#b27a45 70%,#8f5b2e)" role="img" aria-label="Empty room with polished wood floor"></div>
    <div class="txt">
      <h3><span class="arrow">&#9654;</span>WOOD FLOORS<span class="sep">|</span><em>We know how to clean and refinish them.</em></h3>
      <p>If you aren't careful, you may end up with undesirable results when dealing with wood floors. Traditional swing machines can leave swirls if not used correctly, and other methods may damage the wood. We've trained with leading wood floor companies to ensure a process that's safe for your floors and bring you the results you're looking for.</p>
    </div>
  </div>

  <div class="floor-row" style="top:393px;height:57px">
    <div class="photo pic" style="height:47px;background:linear-gradient(90deg,#b9c7d5,#e9eef2 40%,#c23d40 65%,#a3afbb)" role="img" aria-label="Open lobby with red seating on glossy epoxy floor"></div>
    <div class="txt">
      <h3><span class="arrow">&#9654;</span>EPOXY FLOORS<span class="line2">| We Clean Terrazzo, Flake coating, Screeds &amp; More</span></h3>
      <p>Epoxy is protected from chemicals, dirt, liquids and other contaminants, however, Epoxy floors need to be cleaned routinely as they lose their original luster. We can restore any type of Epoxy floor and bring them back to life.</p>
    </div>
  </div>

  <div class="floor-row" style="top:456px;height:57px">
    <div class="photo pic" style="height:47px;background:linear-gradient(#eadfd2,#c98a4a 40%,#b8453a 65%,#d9c7b3)" role="img" aria-label="Cafeteria with chairs on vinyl tile floor"></div>
    <div class="txt">
      <h3><span class="arrow">&#9654;</span>VCT/VINYL FLOORS</h3>
      <p>The most common floor types are our specialty. We can assist you in the maintenance of VCT and vinyl floors. We are helpful resources for assistance with stripping and re coating, daily maintenance, burnishing, and restorative buffing. We have worked with major pad manufacturers and chemical companies to help make selections on the best possible floor maintenance system for these common floors.</p>
    </div>
  </div>
</section>

<section class="page page-bio">
  <h2 class="abs display bio-head">Company Biography</h2>
  <div class="abs bio-copy">
    <p>BrightHollow is a family based company located in the greater Houston area that specializes in commercial floor care and window cleaning. Our mission is to prioritize the health and safety of the people who use your building by offering cleaning methods that are safe and use the latest industry technology. We understand that a clean, well maintained building has a direct relationship with your image - and that can have a direct effect on your bottom line or reputation. Please consider us for further consultation if you are interested in a no obligation discussion about your facility.</p>
    <p>The management of BrightHollow has spent their entire professional lives in the commercial cleaning industry. We have recently sold facility supply distribution company and understand the facility maintenance industry top to bottom. In that time, we've met with innumerable manufacturers, distributors, trade groups, trainers and end users to gain insight into national and regional cleaning trends and methods. We understand budgets, compliance requirements, workflow timelines, and restorative schedules that you don't typically find in a contract cleaning company. We are confident you will benefit from our wide range of experience and expertise when it comes to maintaining your facility.</p>
  </div>
  <div class="brand bio-brand"><span class="dot"></span>BrightHollow</div>
  <div class="photo bio-photo" role="img" aria-label="Modern atrium with glass walkways"></div>
  <div class="abs contact-box"></div>
  <div class="abs display contact-label">Contact</div>
</section>

</body>
</html>
```